We need a business card design for an Afghan catering business called 'Velmi Catering'. We provide Afghan food for any occasions such as wedding, birthday, engagement, small gathering, etc. We would like the business card to include the name of the business designed with the logo, phone number, and the address. We already have our logo that we would upload. The design that we require or suggest must be black with the logo and if possible change the colors of the logo (e.g. the logo includes red and gray lines) to gold. In other words, we would like the business card color to be black with some luxury design that would match the logo. For the front, we would like the logo which includes the name of the business, contact info, and the address. Also, depending on the design we would like to include some pictures of the food. the location (map), facebook, and instagram. After having a look at the design of the business card, we also need menu design and flyer design same thing as the business card design.

Industry/Entity Type

Business

Contact Information for Business Card

Title: Velmi Catering
Phone #: 5550142863 and 5550197214
Name: Lutfiya

Font styles to use
Serif
Script

Colors
000000

Requirements
Must have
• My project must have the name (with the logo), phone number, email, name, address, map, a few picture of the food, facebook, and Instagram logo.
Nice to have
• The color and font must match the logo. It must look simple and luxury (with suggested color black).

```html
<!DOCTYPE html>
<html lang="en">
<head>
<meta charset="utf-8">
<title>Velmi Catering — Business Card</title>
<link href="https://fonts.googleapis.com/css2?family=Lato:wght@400;700;900&display=swap" rel="stylesheet">
<style>
  :root {
    --stage: #2b2b2b;
    --card: #0d0d0d;
    --card-edge: #1a1a1a;
    --gold: #ded018;
    --ink: #0a0a0a;
    --text-soft: #c9c9c9;
    --text-dim: #9a9a9a;
  }
  * { margin: 0; padding: 0; box-sizing: border-box; }
  html, body { width: 1200px; height: 873px; overflow: hidden; }
  body {
    background: var(--stage);
    font-family: "Lato", Arial, sans-serif;
    position: relative;
  }
  .card {
    position: absolute;
    left: 250px;
    width: 700px;
    height: 400px;
    border-radius: 18px;
    background: var(--card);
    border: 1px solid var(--card-edge);
    overflow: hidden;
  }
  .card--front { top: 24px; }
  .card--back { top: 449px; }

  /* brand name */
  .brand {
    color: var(--gold);
    font-weight: 700;
    line-height: 1;
    text-transform: uppercase;
  }
  .brand__name { display: block; letter-spacing: 3px; }
  .brand__sub { display: block; letter-spacing: 4px; }

  /* front */
  .front__brand { position: absolute; left: 120px; top: 95px; text-align: center; }
  .front__brand .brand__name { font-size: 50px; }
  .front__brand .brand__sub { font-size: 19px; margin-top: 6px; }
  .front__divider {
    position: absolute; left: 372px; top: 92px; width: 1px; height: 120px;
    background: linear-gradient(to bottom, transparent, var(--gold), transparent);
    opacity: .6;
  }
  .contact { position: absolute; left: 400px; top: 98px; list-style: none; }
  .contact__item {
    display: flex; align-items: flex-start; gap: 10px;
    color: var(--text-soft); font-size: 15px; line-height: 1.3; margin-bottom: 8px;
  }
  .contact__icon { width: 14px; height: 14px; flex: none; margin-top: 2px; }
  .owner { position: absolute; left: 112px; top: 238px; text-align: center; }
  .owner__name { color: var(--gold); font-weight: 900; font-size: 24px; letter-spacing: 1px; text-transform: uppercase; }
  .owner__role { color: var(--text-soft); font-size: 17px; margin-top: 2px; }
  .owner__email { color: var(--text-dim); font-size: 15px; margin-top: 6px; }
  .front__band {
    position: absolute; left: 0; right: 0; bottom: 0; height: 58px;
    background: var(--gold);
    display: flex; align-items: center; justify-content: flex-end; padding-right: 70px;
  }
  .front__band::before {
    content: ""; position: absolute; left: 0; right: 0; top: 0; height: 8px; background: var(--card);
  }
  .front__web { color: var(--ink); font-weight: 900; font-size: 18px; letter-spacing: 5px; margin-top: 8px; }

  /* back */
  .gallery { position: absolute; left: 0; top: 0; width: 340px; height: 400px; }
  .back__brand { position: absolute; left: 420px; top: 105px; text-align: center; }
  .back__brand .brand__name { font-size: 58px; }
  .back__brand .brand__sub { font-size: 21px; margin-top: 8px; }
  .social { position: absolute; left: 420px; top: 272px; list-style: none; }
  .social__item {
    display: flex; align-items: center; gap: 16px;
    color: var(--gold); font-size: 19px; margin-bottom: 10px;
  }
  .social__mark { width: 24px; height: 24px; border-radius: 4px; background: var(--gold); flex: none; }
</style>
</head>
<body>

<section class="card card--front" aria-label="Business card, contact side">
  <div class="brand front__brand">
    <span class="brand__name">Velmi</span>
    <span class="brand__sub">Catering</span>
  </div>

  <div class="front__divider"></div>

  <ul class="contact">
    <li class="contact__item">
      <svg class="contact__icon" viewBox="0 0 14 14"><path fill="var(--gold)" d="M2 5c0-2 2-3 5-3s5 1 5 3l-2 1-1-2H5L4 6z M3 7h8l1 5H2z"/></svg>
      1-555-014-2863
    </li>
    <li class="contact__item">
      <svg class="contact__icon" viewBox="0 0 14 14"><rect x="1" y="3" width="12" height="9" rx="1" fill="var(--gold)"/><path d="M2 4l5 4 5-4" stroke="var(--card)" stroke-width="1.2" fill="none"/></svg>
      555-019-7214
    </li>
    <li class="contact__item">
      <svg class="contact__icon" viewBox="0 0 14 14"><path fill="var(--gold)" d="M7 1a4 4 0 0 0-4 4c0 3 4 8 4 8s4-5 4-8a4 4 0 0 0-4-4z"/><circle cx="7" cy="5" r="1.5" fill="var(--card)"/></svg>
      <span>1420 Cedar Lane NW,<br>Riverton, OR 97000</span>
    </li>
  </ul>

  <div class="owner">
    <p class="owner__name">Lutfiya</p>
    <p class="owner__role">Owner</p>
    <p class="owner__email">lutfiya@velmicatering.com</p>
  </div>

  <div class="front__band">
    <span class="front__web">www.velmicatering.com</span>
  </div>
</section>

<section class="card card--back" aria-label="Business card, brand side">
  <svg class="gallery" viewBox="0 0 340 400">
    <defs>
      <linearGradient id="dish-kebab" x1="0" y1="0" x2="1" y2="1">
        <stop offset="0" stop-color="#5a2e1c"/><stop offset=".5" stop-color="#b5631f"/><stop offset="1" stop-color="#4a2616"/>
      </linearGradient>
      <linearGradient id="dish-rice" x1="0" y1="0" x2="1" y2="1">
        <stop offset="0" stop-color="#d8cfc0"/><stop offset=".4" stop-color="#d9641c"/><stop offset="1" stop-color="#3a2218"/>
      </linearGradient>
      <linearGradient id="dish-chicken" x1="0" y1="0" x2="1" y2="1">
        <stop offset="0" stop-color="#c9682a"/><stop offset=".5" stop-color="#e0a03a"/><stop offset="1" stop-color="#8a3d1c"/>
      </linearGradient>
    </defs>
    <g role="img" aria-label="Photo of grilled kebab topped with sliced peppers and onions">
      <path d="M12 12 H150 L110 150 H12 Z" fill="url(#dish-kebab)" stroke="url(#dish-kebab)" stroke-width="24" stroke-linejoin="round"/>
    </g>
    <g role="img" aria-label="Photo of a platter of rice with carrots and raisins">
      <path d="M170 40 H320 L272 220 H120 Z" fill="url(#dish-rice)" stroke="url(#dish-rice)" stroke-width="24" stroke-linejoin="round"/>
    </g>
    <g role="img" aria-label="Photo of spiced chicken pieces with peppers and herbs">
      <path d="M12 180 H100 Q130 180 130 210 L104 388 H12 Z" fill="url(#dish-chicken)" stroke="url(#dish-chicken)" stroke-width="24" stroke-linejoin="round"/>
    </g>
  </svg>

  <div class="brand back__brand">
    <span class="brand__name">Velmi</span>
    <span class="brand__sub">Catering</span>
  </div>

  <ul class="social">
    <li class="social__item"><span class="social__mark"></span>velmicatering</li>
    <li class="social__item"><span class="social__mark"></span>velmicatering</li>
  </ul>
</section>

</body>
</html>
```